Lumaridge Hauling

WHY: So we are looking for a clean blue/modern/ mobile friendly website to be able compete with our rival, which is bellhops.comWHO: Our company is based out Atlanta,GA. The Company named is called "LumaRidge Hauling" and we are Professional staffing Agency that trained our employees for Household Industry related tasks such as Moving Furniture, Packers Household Boxes , Vondra Furniture Installers, Mounting TV and etc.WHAT: Our Main Function is we need to be able to pre-qualified lead/schedule them based on availability /Book our client online on Quenpay in order to help our client solve and their problem faster than the traditional 20 min phone call. We need an :Pre-Survey Form /Basic Contact Form Example Below...Desired Button Placement: Should be In the Center or Right Corner. * Q1. What would you like help with? (multi-Choice A to D?* Q2. What are you packing or unpacking* Q3. How many boxes would you like packed or unpacked?* Q4.In Additional to packing or unpacking, do you need any other service>* Q5. Would you like to add photos of the primary item you need packed on..* Q6. When would you like the packing specialist?* Q7. WHat time work best for your schedule?* Q8.Anything else the packing specialist should know? * Q8. Zip Code * Q9. Name* Q10. Email (Privacy Disclaimer)* Q12. Number * Q13. Customer Credit Card InfoWHEN: we looking to be done submit all of our revision request and the project done before New Year, Jan.1

Target Market(s)

Womans: Between 25yr to +55 Womans, Affluence,

Industry/Entity Type

Moving

Number of Pages Required

2 page

Font styles to use
Sans Serif

Colors

Designer to choose colors to be used in the design.

Requirements
Must have
• Service Option Category
• Packers/Installer/ Rental Trucks Assistant
• How it Work Session
• 1.Pick a Service
• 2.Book A Time
• 3.Secured A Payment
Nice to have
• Our Main Function is we need to be able to pre-qualified lead/schedule them based on availability /Book our client online on Quenpay in order to help our client solve and their problem faster than the traditional 20 min phone call.
• We need an :Pre-Survey Form /Basic Contact Form Example Below...
• Desired Button Placement: Should be In the Center or Right Corner.
• * Q1. What would you like help with? (multi-Choice A to D?
• * Q2. What are you packing or unpacking
• * Q3. How many boxes would you like packed or unpacked?
• * Q4.In Additional to packing or unpacking, do you need any other service>
• * Q5. Would you like to add photos of the primary item you need packed on..
• * Q6. When would you like the packing specialist?
• * Q7. WHat time work best for your schedule?
• * Q8.Anything else the packing specialist should know?
• * Q8. Zip Code
• * Q9. Name
• * Q10. Email (Privacy Disclaimer)
• * Q12. Number
• * Q13. Customer Credit Card Info
Should not have
• we are not interesting for an Basic Template Design /generic Truck photo stock/ traditional moving company website).

```html
<!DOCTYPE html>
<html lang="en">
<head>
<meta charset="utf-8">
<title>LumaRidge Hauling</title>
<link href="https://fonts.googleapis.com/css2?family=Raleway:wght@300;400;600;700;800&family=Open+Sans:wght@400;600;700&display=swap" rel="stylesheet">
<style>
:root{
  --blue:#3f7ef0;
  --blue-dark:#2d66d6;
  --ink:#111216;
  --text:#5d6270;
  --muted:#9aa0ab;
  --grey:#f0f1f4;
  --line:#e2e5ea;
  --mint:#e6f1de;
  --white:#fff;
}
*{box-sizing:border-box;margin:0;padding:0}
html,body{width:1200px;height:4535px;overflow:hidden}
body{position:relative;background:var(--white);font-family:"Open Sans",Arial,sans-serif;color:var(--text);font-size:13px}
.abs{position:absolute}
h1,h2,h3,h4,.nav,.btn{font-family:"Raleway",Arial,sans-serif}
.btn{display:inline-block;background:var(--blue);color:#fff;font-weight:700;font-size:12px;text-transform:uppercase;text-align:center;border-radius:3px}
.photo{position:absolute}

/* top bar + header */
.topbar{left:0;top:0;width:1200px;height:30px;background:var(--blue);color:#fff;font-size:11px}
.topbar span{position:absolute;top:8px}
.header{left:0;top:30px;width:1200px;height:87px;background:#fff}
.logo{left:128px;top:26px;font-family:"Raleway",sans-serif;font-weight:800;font-size:30px;color:var(--ink);letter-spacing:-.5px}
.nav{left:425px;top:34px;display:flex;gap:30px;font-size:12px;font-weight:700;color:#333;text-transform:uppercase}
.nav .active{color:var(--blue)}
.quote{left:944px;top:24px;width:136px;height:40px;line-height:40px}

/* hero */
.hero{left:0;top:117px;width:1200px;height:600px;background:linear-gradient(110deg,#8a6c52 0%,#c7a98b 30%,#e3d2bd 55%,#b59477 80%,#6f5845 100%)}
.hero-shade{left:0;top:117px;width:1200px;height:600px;background:rgba(20,22,30,.45)}
.hero-title{left:0;top:325px;width:1200px;text-align:center;color:#fff;font-size:38px;font-weight:700}
.hero-text{left:300px;top:400px;width:600px;text-align:center;color:#fff;font-size:14px;line-height:24px}
.hero-btn{left:537px;top:468px;width:126px;height:40px;line-height:40px}
.arrow{color:#fff;font-size:34px;font-weight:300;top:380px}

/* booking */
.booking{left:130px;top:595px;width:940px;height:212px;background:#fff;box-shadow:0 6px 24px rgba(0,0,0,.12);border-radius:3px}
.field{position:absolute;width:200px}
.field label{display:block;font-size:12px;font-weight:700;color:#222;margin-bottom:8px}
.field div{height:40px;border:1px solid var(--line);border-radius:3px;padding:0 12px;line-height:38px;color:var(--muted);font-size:12px}
.field div.val{color:#333}
.b-more{left:520px;top:135px;width:200px;height:42px;line-height:42px;background:var(--ink)}
.b-book{left:732px;top:135px;width:190px;height:42px;line-height:42px}

/* services */
.svc{width:258px;height:150px;background:#fff;box-shadow:0 4px 18px rgba(0,0,0,.1);text-align:center;padding:16px 22px}
.svc .ico{width:44px;height:40px;margin:0 auto 8px;border-radius:4px}
.svc h4{font-size:15px;font-weight:700;color:#222;margin-bottom:8px}
.svc p{font-size:11px;line-height:17px}
.tag{background:var(--ink);color:#fff;font-size:10px;padding:4px 10px;font-family:"Raleway",sans-serif;font-weight:600}
.main-title{left:710px;top:915px;font-family:"Raleway",sans-serif;font-size:44px;line-height:46px;font-weight:800;color:var(--ink)}
.main-title b{color:var(--blue)}
.main-title span{display:block;color:var(--blue);font-weight:300}
.main-text{left:710px;top:1015px;width:340px;font-size:11px;line-height:19px}

/* section headings */
.sh{left:0;width:1200px;text-align:center}
.sh h2{font-size:44px;font-weight:800;color:var(--ink);text-transform:uppercase}
.sh h2 em{font-style:normal;color:var(--blue)}
.sh h2 i{font-style:normal;font-weight:300;color:var(--blue)}
.sh p{width:520px;margin:10px auto 0;font-size:13px;line-height:21px}

/* story */
.story-bg{left:196px;top:1595px;width:390px;height:330px;background:var(--mint)}
.story-img{left:130px;top:1595px;width:456px;height:282px;background:linear-gradient(135deg,#6f8e5a,#c9b08a 55%,#8d6b4b)}
.story-text{left:626px;top:1630px;width:440px}
.story-text h3{font-size:20px;font-weight:700;color:var(--blue);margin-bottom:12px}
.story-text p{font-size:12px;line-height:21px;margin-bottom:10px}

/* why */
.why-title{left:173px;top:2090px;font-family:"Raleway",sans-serif;font-size:44px;font-weight:800;color:#fff}
.why-title b{color:var(--ink)}
.why-text{left:180px;top:2165px;width:330px;color:#dfe8ff;font-size:12px;line-height:21px;text-align:right}
.video{left:546px;top:2036px;width:537px;height:231px;background:linear-gradient(120deg,#c9c2b8,#ece8e2 50%,#a9a096)}
.play{left:788px;top:2122px}

/* process */
.proc-text{left:250px;top:2630px;width:700px;text-align:center;color:#d4d6dc;font-size:13px;line-height:22px}
.step{width:240px;text-align:center;color:#fff;font-family:"Raleway",sans-serif;font-weight:700;font-size:13px;text-transform:uppercase}

/* testimonials */
.testi{width:500px;height:160px;background:var(--mint);padding:10px}
.testi div{background:#fff;height:140px;padding:18px 26px}
.testi p{font-size:12px;line-height:20px;color:#333}
.testi h4{margin-top:12px;font-size:12px;color:var(--blue);font-weight:700}
.testi small{font-size:11px;color:var(--muted)}
.avatar{width:56px;height:56px;border-radius:50%;background:linear-gradient(135deg,#bfc3c9,#8a8f98)}

/* team */
.team-bg{left:0;top:3540px;width:1200px;height:600px;background:var(--grey)}
.member{width:216px;height:288px;background:#fff}
.member .pic{height:288px;background:linear-gradient(160deg,#e7e9ed,#c5b79e 60%,#8f7a5f)}
.member .cap{position:absolute;left:80px;bottom:-12px;width:136px;height:58px;background:#fff;padding:10px 12px;box-shadow:0 3px 10px rgba(0,0,0,.1)}
.member h4{font-size:12px;color:var(--blue);font-weight:700}
.member small{font-size:10px;color:var(--muted)}
.tarrow{width:36px;height:36px;background:#fff;box-shadow:0 2px 8px rgba(0,0,0,.12);text-align:center;line-height:36px;color:#333;top:3905px}

/* footer */
.footer{left:0;top:4134px;width:1200px;height:371px;background:#15161a;color:#c8cad0}
.fcol{position:absolute;top:64px;font-size:12px;line-height:22px}
.fcol h4{color:#fff;font-size:12px;font-weight:700;text-transform:uppercase;margin-bottom:14px}
.copy{left:0;top:4505px;width:1200px;height:30px;background:#0b0b0d;color:#8b8e96;font-size:10px;padding:9px 0 0 162px}
</style>
</head>
<body>

<div class="abs topbar">
  <span style="left:815px">&#9742; +1 404 555 0182</span>
  <span style="left:958px">&#9993; hello@lumaridge.example</span>
</div>

<header class="abs header">
  <div class="abs logo">LumaRidge</div>
  <nav class="abs nav">
    <span class="active">Home</span><span>About Us</span><span>Reviews</span><span>FAQ'S</span><span>Services</span><span>Contact Us</span>
  </nav>
  <span class="abs btn quote">Get Free Quote</span>
</header>

<section>
  <div class="photo hero" role="img" aria-label="Photo of a smiling man carrying a moving box in a bright home"></div>
  <div class="abs hero-shade"></div>
  <h1 class="abs hero-title">Book A Local LumaRidge Athete</h1>
  <p class="abs hero-text">When your home is packed and your day is full, our trained crew arrives on time to lift, pack and set up. We make every move calm, careful and quick.</p>
  <span class="abs btn hero-btn">Learn More</span>
  <span class="abs arrow" style="left:30px">&#8249;</span>
  <span class="abs arrow" style="left:1150px">&#8250;</span>
  <svg class="abs" style="left:0;top:600px" width="1200" height="120" viewBox="0 0 1200 120" preserveAspectRatio="none">
    <path d="M0 60 C300 110 600 110 900 70 C1020 55 1120 40 1200 30 L1200 120 L0 120 Z" fill="#fff"/>
  </svg>
</section>

<section class="abs booking">
  <div class="field" style="left:22px;top:30px"><label>Enter your name</label><div>Ex: Jonathan</div></div>
  <div class="field" style="left:270px;top:30px"><label>Phone number</label><div>Ex: 404 555 0100</div></div>
  <div class="field" style="left:520px;top:30px"><label>Date</label><div class="val">10 - 04 - 2019 &#9662;</div></div>
  <div class="field" style="left:732px;top:30px;width:190px"><label>What would you like help with?</label><div class="val">Household things &#9662;</div></div>
  <div class="field" style="left:22px;top:110px"><label>Move From</label><div class="val">New York &#9662;</div></div>
  <div class="field" style="left:270px;top:110px"><label>Move To</label><div class="val">Jax New York &#9662;</div></div>
  <span class="abs btn b-more">More Options</span>
  <span class="abs btn b-book">Book Now</span>
</section>

<svg class="abs" style="left:0;top:1130px" width="1200" height="190" viewBox="0 0 1200 190" preserveAspectRatio="none">
  <path d="M0 60 L1200 0 L1200 120 L0 190 Z" fill="#f0f1f4"/>
</svg>

<section>
  <div class="abs svc" style="left:130px;top:873px"><div class="ico" style="background:#e6a43c" role="img" aria-label="Stacked boxes icon"></div><h4>Packing / Boxes</h4><p>Every item wrapped, boxed and labelled by a trained packer who knows fragile.</p></div>
  <div class="abs svc" style="left:410px;top:873px"><div class="ico" style="background:#e2533f" role="img" aria-label="Rental truck icon"></div><h4>Pack Rental / Truck</h4><p>We load and unload your rented truck so every room arrives in one piece.</p></div>
  <div class="abs svc" style="left:130px;top:1040px"><div class="ico" style="background:#3aa0d8" role="img" aria-label="Packed pods icon"></div><h4>PACKED PODS</h4><p>Pods filled tight and safe, ready for storage or the road.</p></div>
  <div class="abs svc" style="left:410px;top:1040px"><div class="ico" style="background:#5b6b86" role="img" aria-label="Installation tools icon"></div><h4>INSTALLATION</h4><p>Furniture built, TVs mounted and shelves set level in your new space.</p></div>
  <span class="abs tag" style="left:712px;top:893px">What We Offer</span>
  <h2 class="abs main-title">OUR <b>MAINCORE</b><span>SERVICE</span></h2>
  <p class="abs main-text">We strongly believe that careful hands build trust. Every move is planned around you, your home and your time, so the people you love can settle in sooner.</p>
</section>

<section>
  <div class="sh abs" style="top:1410px"><span class="tag">What We Do</span></div>
  <div class="sh abs" style="top:1438px">
    <h2>The Story <i>About Us</i></h2>
    <p>We started with one truck and a promise to treat each home as our own. Today our crew serves families across Atlanta.</p>
  </div>
  <div class="abs story-bg"></div>
  <div class="photo story-img" role="img" aria-label="Photo of a family carrying moving boxes outside their new house"></div>
  <div class="abs story-text">
    <h3>LUMARIDGE</h3>
    <p>We strongly believe that trained, trusted people are the heart of every move. Our crew, our clients and our city all grow when the job is done right.</p>
    <p>Our Movers Are Trained And Vetted.<br>Why do we always come back to you?<br>There are no hidden fees at all.<br>Those Happy Days are yours and mine Happy Days.</p>
  </div>
</section>

<svg class="abs" style="left:0;top:1920px" width="1200" height="500" viewBox="0 0 1200 500" preserveAspectRatio="none">
  <path d="M0 40 C300 0 500 50 800 30 C1000 15 1120 10 1200 0 L1200 430 L0 470 Z" fill="#3f7ef0"/>
</svg>
<section>
  <span class="abs tag" style="left:372px;top:2048px">See Our Expertise</span>
  <h2 class="abs why-title">WHY <b>CHOOSE</b> US</h2>
  <p class="abs why-text">We offer a wide range of moving services and handle each piece with care, from single rooms to full homes. Our crew packs, lifts and installs so you can focus on the life ahead, not the boxes around you.</p>
  <div class="photo video" role="img" aria-label="Video still of a mover carrying a white sofa"></div>
  <svg class="abs play" width="56" height="56" viewBox="0 0 56 56"><circle cx="28" cy="28" r="28" fill="#fff"/><path d="M22 17 L40 28 L22 39 Z" fill="#111216"/></svg>
</section>

<svg class="abs" style="left:0;top:2370px" width="1200" height="620" viewBox="0 0 1200 620" preserveAspectRatio="none">
  <path d="M0 40 L1200 0 L1200 540 L0 610 Z" fill="#111216"/>
</svg>
<section>
  <div class="sh abs" style="top:2540px"><h2 style="color:#fff;font-size:38px"><em>OUR</em> WORK <i>PROCESS</i></h2></div>
  <p class="abs proc-text">We strongly believe that your time matters. Three simple steps take you from first click to a booked, paid crew at your door, with no long phone calls.</p>
  <svg class="abs" style="left:0;top:2715px" width="1200" height="110" viewBox="0 0 1200 110">
    <line x1="235" y1="55" x2="1000" y2="55" stroke="#3f7ef0" stroke-width="1" stroke-dasharray="3 6"/>
    <circle cx="235" cy="55" r="50" fill="#3f7ef0"/>
    <rect x="222" y="36" width="26" height="34" rx="2" fill="none" stroke="#fff" stroke-width="3"/>
    <path d="M228 48 h14 M228 56 h14" stroke="#fff" stroke-width="2"/>
    <circle cx="600" cy="55" r="50" fill="#3f7ef0"/>
    <circle cx="600" cy="55" r="18" fill="none" stroke="#fff" stroke-width="3"/>
    <path d="M600 44 V55 H609" stroke="#fff" stroke-width="3" fill="none"/>
    <circle cx="965" cy="55" r="50" fill="#3f7ef0"/>
    <rect x="945" y="40" width="40" height="28" rx="3" fill="none" stroke="#fff" stroke-width="3"/>
    <path d="M945 49 h40" stroke="#fff" stroke-width="4"/>
  </svg>
  <div class="abs step" style="left:115px;top:2845px">Pick A Service</div>
  <div class="abs step" style="left:480px;top:2845px">Book A Time</div>
  <div class="abs step" style="left:845px;top:2845px">Secured A Payment</div>
</section>

<section>
  <div class="sh abs" style="top:3010px"><span class="tag">What They Say About Us</span></div>
  <div class="sh abs" style="top:3040px">
    <h2><em>CLIENT</em> TESTIMONIAL</h2>
    <p>Families trust us with the things that matter most. Here is what a few of them had to say after moving day.</p>
  </div>
  <div class="abs testi" style="left:136px;top:3232px"><div>
    <p>They arrived early, wrapped every frame and had our kitchen unpacked before dinner. The calmest move we have ever had.</p>
    <h4>MARA ELLISON</h4><small>Homeowner, Decatur</small></div></div>
  <div class="abs testi" style="left:646px;top:3232px"><div>
    <p>A real relief when the crew knows the job. Booking took two minutes online and the team set up our beds and TV in one visit.</p>
    <h4>TESSA VOIGHT</h4><small>Homeowner, Midtown</small></div></div>
  <div class="abs avatar" style="left:178px;top:3410px" role="img" aria-label="Client portrait"></div>
  <div class="abs avatar" style="left:662px;top:3410px" role="img" aria-label="Client portrait"></div>
  <svg class="abs" style="left:555px;top:3500px" width="100" height="6"><rect x="0" y="0" width="28" height="4" fill="#3f7ef0"/><rect x="36" y="0" width="28" height="4" fill="#c9ccd2"/><rect x="72" y="0" width="28" height="4" fill="#c9ccd2"/></svg>
</section>

<svg class="abs" style="left:0;top:3520px" width="1200" height="60" viewBox="0 0 1200 60" preserveAspectRatio="none"><path d="M0 60 C400 0 800 0 1200 40 L1200 60 Z" fill="#f0f1f4"/></svg>
<section>
  <div class="abs team-bg"></div>
  <div class="sh abs" style="top:3632px"><span class="tag">What They Are About Us</span></div>
  <div class="sh abs" style="top:3660px">
    <h2><em>LUMARIDGE</em> TEAM</h2>
    <p>Meet the trained crew leads who plan, pack and install for every home we serve.</p>
  </div>
  <div class="abs member" style="left:130px;top:3779px"><div class="pic" role="img" aria-label="Photo of a mover in a cap holding a box"></div><div class="cap"><h4>DARIUS KELL</h4><small>Crew Lead</small></div></div>
  <div class="abs member" style="left:453px;top:3779px"><div class="pic" role="img" aria-label="Photo of a mover in a hard hat carrying boxes"></div><div class="cap"><h4>OWEN PRATT</h4><small>Packing Lead</small></div></div>
  <div class="abs member" style="left:771px;top:3779px"><div class="pic" role="img" aria-label="Photo of a team member holding a tablet"></div><div class="cap"><h4>NINA SOREL</h4><small>Client Planner</small></div></div>
  <div class="abs tarrow" style="left:68px">&#8249;</div>
  <div class="abs tarrow" style="left:1132px">&#8250;</div>
</section>

<footer class="abs footer" role="contentinfo">
  <div class="fcol" style="left:162px;width:230px">
    <h4>Get In Touch</h4>
    <p>&#9906; 48 Harlow Bend, Suite 2,<br>&nbsp;&nbsp;&nbsp;Atlanta GA 30318,<br>&nbsp;&nbsp;&nbsp;Mon - Sat 08:00 - 18:00</p>
    <p style="margin-top:14px;font-size:14px">&#9742; (404) 555-0147</p>
    <p style="margin-top:10px">&#9993; hello@lumaridge.example</p>
  </div>
  <div class="fcol" style="left:432px">
    <h4>Company Links</h4>
    <p>Local Moves<br>International Moves<br>Long Distance<br>Auto Transport<br>Packing/Unpacking<br>Storage/Moving<br>Household moving</p>
  </div>
  <div class="fcol" style="left:622px">
    <h4>Newsletter Signup</h4>
    <p style="font-size:10px;line-height:15px">If you want to get all our weekly<br>updates subscribe here.</p>
    <svg style="margin-top:16px" width="196" height="34"><rect width="170" height="34" fill="#fff"/><rect x="170" width="26" height="34" fill="#3f7ef0"/><path d="M177 17 L190 11 L186 24 Z" fill="#fff"/></svg>
  </div>
  <div class="fcol" style="left:876px">
    <h4>Social Links</h4>
    <svg width="190" height="26"><rect x="0" width="26" height="26" fill="#3f7ef0"/><rect x="32" width="26" height="26" fill="#3f7ef0"/><rect x="64" width="26" height="26" fill="#3f7ef0"/><rect x="96" width="26" height="26" fill="#3f7ef0"/><rect x="128" width="26" height="26" fill="#3f7ef0"/></svg>
  </div>
</footer>
<div class="abs copy">&copy; Copyright 2019 lumaridge.example. All rights reserved</div>

</body>
</html>
```